KOV Business Card

the business card should be double sided.
Will need to be Korean on one side and english on the other.
it will need to have:

address
website
skype
phone
cell
fax
name
title
email

just put in dummy details to start - i will then give you correct info once we have the format right.

Also - if you feel creative about the logo we are happy to make some amendments to it so it looks right. We are still at early stages with the logo so happy if you have suggestions around the logo concept.
Updates

The deadline for this has been brought forward to Wednesday 11th December. We can not review any designs after this date.

we will need to make a decision by Wednesday 11th December, so please have designs in by this date and not by the deadline set by craftfolio

Target Market(s)

large companies, executives

Industry/Entity Type

Business

Colors

Designer to choose colors to be used in the design.

Requirements
Must have
• double sided - english on one side and korean on the other. we will give you korean wording once we have a design we like.

```html
<!DOCTYPE html>
<html lang="en">
<head>
<meta charset="utf-8">
<title>KOV Business Card</title>
<link rel="stylesheet" href="https://fonts.googleapis.com/css2?family=PT+Sans:wght@400;700&display=swap">
<style>
  :root {
    --brand-blue: #0f4c9c;
    --ink: #333333;
    --swoosh-dark: #555558;
    --swoosh-light: #8a8a8e;
    --card-white: #ffffff;
    --backdrop: #e9e9e9;
    --divider: #c8c8c8;
  }
  * { box-sizing: border-box; margin: 0; padding: 0; }
  html, body { width: 1200px; height: 480px; overflow: hidden; }
  body {
    background: var(--backdrop);
    font-family: "PT Sans", sans-serif;
    color: var(--ink);
    position: relative;
  }
  .card {
    position: absolute;
    top: 90px;
    width: 520px;
    height: 300px;
    overflow: hidden;
    box-shadow: 0 2px 8px rgba(0,0,0,0.15);
  }
  .card--front { left: 60px; background: var(--card-white); }
  .card--back {
    left: 620px;
    background: var(--brand-blue);
    display: flex;
    align-items: center;
    justify-content: center;
  }
  .brand {
    position: absolute;
    left: 38px;
    top: 44px;
    width: 200px;
  }
  .brand__name {
    font-size: 72px;
    font-weight: 700;
    line-height: 1;
    color: var(--brand-blue);
    letter-spacing: 2px;
  }
  .brand__web {
    font-size: 11px;
    color: var(--swoosh-dark);
    letter-spacing: 0.5px;
    text-align: right;
    margin-top: 2px;
    padding-right: 24px;
  }
  .divider {
    position: absolute;
    left: 252px;
    top: 20px;
    width: 1px;
    height: 130px;
    background: var(--divider);
  }
  .contact {
    position: absolute;
    left: 268px;
    top: 20px;
    font-size: 13px;
    line-height: 17px;
    list-style: none;
  }
  .contact__label { color: var(--brand-blue); font-weight: 700; display: inline-block; width: 14px; }
  .contact__skype { color: var(--brand-blue); margin-top: 4px; }
  .address { position: absolute; left: 284px; top: 120px; font-size: 13px; line-height: 17px; }
  .swoosh { position: absolute; left: 0; top: 0; }
  .holder {
    position: absolute;
    left: 28px;
    bottom: 14px;
    color: var(--card-white);
    font-size: 20px;
  }
  .holder__title { font-size: 15px; }
  .back-brand {
    color: var(--card-white);
    font-size: 76px;
    font-weight: 700;
    letter-spacing: 3px;
  }
</style>
</head>
<body>
  <section class="card card--front">
    <svg class="swoosh" width="520" height="300" viewBox="0 0 520 300" aria-hidden="true">
      <path d="M0 222 Q250 184 520 166 L520 177 Q256 194 0 234 Z" fill="var(--swoosh-dark)"/>
      <path d="M0 240 Q256 200 520 183 L520 190 Q262 208 0 248 Z" fill="var(--swoosh-light)"/>
      <path d="M0 254 Q262 214 520 196 L520 300 L0 300 Z" fill="var(--brand-blue)"/>
    </svg>
    <div class="brand">
      <div class="brand__name">KOV</div>
      <div class="brand__web">WWW.KOVSITE.COM</div>
    </div>
    <div class="divider"></div>
    <ul class="contact">
      <li><span class="contact__label">P</span>: 012.345.6789</li>
      <li><span class="contact__label">M</span>: 012.345.6789</li>
      <li><span class="contact__label">F</span>: 012.345.6789</li>
      <li><span class="contact__label">E</span>: info@kovsite.com</li>
      <li class="contact__skype">Skype: infokov</li>
    </ul>
    <p class="address">Suite 000, 000 building,<br>Cityname, country name</p>
    <p class="holder">YOURNAME HERE, <span class="holder__title">Director</span></p>
  </section>

  <section class="card card--back">
    <div class="back-brand">KOV</div>
  </section>
</body>
</html>
```